VELINTA Promotions - Business Card Design Project

We are looking for a classy business cards for Promotion Company based in Toronto, Canada named Velinta Promotions.

Velinta Promotions has an idea and vision to set high standard, be EXCLUSIVE and attract a group of people that will follow us through events we promote (night clubs, brand promotions, music events, and sport events)

We want to present a high standards and classy image to the others...
Updates

Target Market(s)

male/female age 25-40 Target: business owners young entrepreneur - clubing industry - media industry - promotion industry - marketing media industry

Industry/Entity Type

Events

Requirements
Must have
• business cards should be classy, make people feel exclusive , make people react ..

```html
<!DOCTYPE html>
<html lang="en">
<head>
<meta charset="utf-8">
<title>Velinta Promotions – Business Card Concepts</title>
<link rel="stylesheet" href="https://fonts.googleapis.com/css2?family=Cormorant+Garamond:wght@400;500;600&family=Great+Vibes&display=swap">
<style>
  :root {
    --ink: #000000;
    --paper: #ffffff;
    --cyan: #1fb6e0;
    --grey: #3a3a3a;
    --rule: #c8c8c8;
    --serif: "Cormorant Garamond", Georgia, serif;
    --script: "Great Vibes", cursive;
  }
  * { margin: 0; padding: 0; box-sizing: border-box; }
  html, body { width: 1200px; height: 1000px; overflow: hidden; background: var(--paper); }
  .sheet { position: relative; width: 1200px; height: 1000px; }

  .card { position: absolute; width: 598px; height: 330px; overflow: hidden; font-family: var(--serif); }
  .card--dark { background: var(--ink); color: var(--paper); }
  .card--light { background: var(--paper); color: var(--grey); border: 1px solid var(--rule); }
  .card .sweep { position: absolute; inset: 0; width: 100%; height: 100%; }

  .pos-a { left: 0; top: 0; }
  .pos-b { left: 602px; top: 0; }
  .pos-c { left: 0; top: 335px; }
  .pos-d { left: 602px; top: 335px; }
  .pos-e { left: 0; top: 670px; }
  .pos-f { left: 602px; top: 670px; }

  .brand { position: absolute; display: flex; align-items: center; gap: 10px; color: var(--cyan); font-weight: 500; letter-spacing: 2px; white-space: nowrap; }
  .brand__mark { width: 0.7em; height: 0.7em; background: var(--cyan); }

  .flourish { position: absolute; width: 80px; height: 62px; background: radial-gradient(circle, rgba(31,182,224,0.35), rgba(31,182,224,0) 70%); }

  .script-name { font-family: var(--script); color: var(--cyan); font-weight: 400; white-space: nowrap; }
  .caps-name { color: var(--cyan); font-variant: small-caps; font-weight: 500; letter-spacing: 1px; white-space: nowrap; }
  .role { font-size: 13px; letter-spacing: 4px; text-transform: uppercase; white-space: nowrap; }
  .contact { font-size: 15px; line-height: 1.45; white-space: nowrap; }
  .contact .hi { color: var(--cyan); }
  .contact .plain { color: var(--ink); }

  .centered { position: absolute; left: 0; right: 0; text-align: center; }

  .tilt { position: absolute; transform-origin: left top; }
  .tilt--right { transform-origin: right top; text-align: right; }
</style>
</head>
<body>
<main class="sheet">

  <!-- Concept 1: centred black card -->
  <section class="card card--dark pos-a">
    <div class="flourish" style="left:8px;top:8px" role="img" aria-label="Swirl ornament"></div>
    <div class="flourish" style="right:8px;top:8px" role="img" aria-label="Swirl ornament"></div>
    <div class="flourish" style="left:8px;bottom:8px" role="img" aria-label="Swirl ornament"></div>
    <div class="flourish" style="right:8px;bottom:8px" role="img" aria-label="Swirl ornament"></div>
    <div class="brand" style="left:150px;top:42px;font-size:38px"><span class="brand__mark"></span>VELINTA Promotions</div>
    <div class="centered script-name" style="top:140px;font-size:56px">Daniel Reyes</div>
    <div class="centered role" style="top:204px">Managing Director</div>
    <div class="centered contact" style="top:243px">
      <div class="hi">4521 Marlowe Ave., Toronto, Canada</div>
      <div class="hi">ph.: 416 555 0192, mob.: 647 555 0148</div>
      <div>inbox@velinta.com | www.velinta.com</div>
    </div>
  </section>

  <!-- Concept 2: white card with black sweep -->
  <section class="card card--light pos-b">
    <svg class="sweep" viewBox="0 0 598 330" preserveAspectRatio="none" aria-hidden="true">
      <path d="M0 0 H598 V0 C540 70 420 120 260 150 C160 168 70 178 0 182 Z" fill="var(--ink)"/>
    </svg>
    <div class="brand tilt" style="left:34px;top:80px;font-size:32px;transform:rotate(-8deg)"><span class="brand__mark"></span>VELINTA Promotions</div>
    <div class="tilt" style="left:76px;top:228px;transform:rotate(-13deg)">
      <div class="caps-name" style="font-size:32px">Daniel Reyes</div>
      <div class="role" style="margin-left:60px;margin-top:4px">Managing Director</div>
    </div>
    <div class="tilt tilt--right contact" style="right:32px;top:172px;transform:rotate(-16deg)">
      <div class="hi">ph.: 416 555 0192, mob.: 647 555 0148</div>
      <div class="hi">4521 Marlowe Ave., Toronto, Canada</div>
      <div class="plain">inbox@velinta.com | www.velinta.com</div>
    </div>
  </section>

  <!-- Concept 3: white card, black corner, centred script -->
  <section class="card card--light pos-c">
    <svg class="sweep" viewBox="0 0 598 330" preserveAspectRatio="none" aria-hidden="true">
      <path d="M0 0 H345 C300 80 200 140 0 168 Z" fill="var(--ink)"/>
    </svg>
    <div class="brand" style="left:26px;top:56px;font-size:19px;gap:7px;letter-spacing:1.5px"><span class="brand__mark"></span>VELINTA Promotions</div>
    <div class="centered script-name" style="top:140px;font-size:54px">Daniel Reyes</div>
    <div class="centered role" style="top:208px">Managing Director</div>
    <div class="centered contact" style="top:245px">
      <div class="hi">4521 Marlowe Ave., Toronto, Canada</div>
      <div class="hi">ph.: 416 555 0192, mob.: 647 555 0148</div>
      <div class="plain">inbox@velinta.com | www.velinta.com</div>
    </div>
  </section>

  <!-- Concept 4: black card, tilted layout -->
  <section class="card card--dark pos-d">
    <div class="brand tilt" style="left:34px;top:72px;font-size:38px;transform:rotate(-8deg)"><span class="brand__mark"></span>VELINTA Promotions</div>
    <div class="tilt" style="left:76px;top:228px;transform:rotate(-13deg)">
      <div class="caps-name" style="font-size:32px">Daniel Reyes</div>
      <div class="role" style="margin-left:60px;margin-top:4px">Managing Director</div>
    </div>
    <div class="tilt tilt--right contact" style="right:32px;top:168px;transform:rotate(-16deg)">
      <div class="hi">ph.: 416 555 0192, mob.: 647 555 0148</div>
      <div class="hi">4521 Marlowe Ave., Toronto, Canada</div>
      <div>inbox@velinta.com | www.velinta.com</div>
    </div>
  </section>

  <!-- Concept 5: white card, steep diagonal -->
  <section class="card card--light pos-e">
    <svg class="sweep" viewBox="0 0 598 330" preserveAspectRatio="none" aria-hidden="true">
      <path d="M0 0 H468 C430 110 280 180 0 192 Z" fill="var(--ink)"/>
    </svg>
    <div class="brand" style="left:30px;top:30px;font-size:34px"><span class="brand__mark"></span>VELINTA Promotions</div>
    <div class="tilt" style="left:162px;top:235px;transform:rotate(-30deg)">
      <div class="caps-name" style="font-size:30px;line-height:36px;margin-left:84px">Daniel Reyes</div>
      <div class="role" style="line-height:20px;margin-left:134px">Managing Director</div>
      <div class="contact" style="margin-top:10px">
        <div class="hi">4521 Marlowe Ave., Toronto, Canada</div>
        <div class="hi" style="margin-left:70px">ph.: 416 555 0192, mob.: 647 555 0148</div>
        <div class="plain" style="margin-left:150px">inbox@velinta.com | www.velinta.com</div>
      </div>
    </div>
  </section>

  <!-- Concept 6: black card, large brand and tilt -->
  <section class="card card--dark pos-f">
    <div class="brand tilt" style="left:34px;top:70px;font-size:46px;transform:rotate(-8deg)"><span class="brand__mark"></span>VELINTA Promotions</div>
    <div class="tilt" style="left:76px;top:226px;transform:rotate(-10deg)">
      <div class="caps-name" style="font-size:30px">Daniel Reyes</div>
      <div class="role" style="margin-left:50px;margin-top:2px">Managing Director</div>
    </div>
    <div class="tilt tilt--right contact" style="right:28px;top:170px;transform:rotate(-16deg)">
      <div class="hi">ph.: 416 555 0192, mob.: 647 555 0148</div>
      <div class="hi">4521 Marlowe Ave., Toronto, Canada</div>
      <div>inbox@velinta.com | www.velinta.com</div>
    </div>
  </section>

</main>
</body>
</html>
```